Mavi'd Food Menu

We are a 100% Organic Juice Bar and are launching an organic vegan food menu. We need a new menu designed for the food listed on the file "Breakfast&Lunch Menu"

We also need our original menu revised to match the style of the vegan food menu. This information can be found on the file "Mavid Menu Summer 2017"

Requirements
Must have
• 2 files. One for Breakfast & Lunch Food Menu and one for our current menu which is also attached. Breakfast/Lunch Menu will be printed on a 9.5" by 11" and the current menu on legal size paper (This menu can be double sided like original)

```html
<!DOCTYPE html>
<html lang="en">
<head>
<meta charset="utf-8">
<title>Mavid Breakfast Menu</title>
<link href="https://fonts.googleapis.com/css2?family=Alegreya+Sans+SC:wght@700;800&family=Raleway:wght@400;500&family=Handlee&family=Kaushan+Script&display=swap" rel="stylesheet">
<style>
  :root {
    --page-bg: #efeee6;
    --paper-top: #fdfde9;
    --paper-mid: #eef5c6;
    --paper-low: #d3eaa4;
    --title-green: #2d5a12;
    --accent-green: #3f7d1c;
    --ink: #3a3a2c;
    --heading-ink: #26261a;
    --brown: #8a5a2b;
    --rule: #8f9384;
    --food-warm: #c9a56e;
    --food-green: #8dbb5a;
  }
  * { box-sizing: border-box; margin: 0; padding: 0; }
  html, body { width: 1200px; height: 1200px; overflow: hidden; background: var(--page-bg); }
  .menu {
    position: absolute; left: 96px; top: 15px;
    width: 1120px; height: 1300px;
    transform: scale(0.9); transform-origin: 0 0;
    background: linear-gradient(180deg, var(--paper-top) 0%, #f6f9d8 25%, var(--paper-mid) 50%, var(--paper-low) 85%, #dcefb4 100%);
    font-family: 'Raleway', sans-serif; color: var(--ink);
    box-shadow: 0 4px 18px rgba(0,0,0,.18);
  }
  .leaves { position: absolute; background: linear-gradient(135deg, rgba(140,198,63,.35), rgba(140,198,63,.15)); border-radius: 40% 60% 50% 50%; }
  .brand { position: absolute; left: 395px; top: 135px; width: 370px; text-align: center;
    font-family: 'Alegreya Sans SC', sans-serif; font-weight: 800; font-size: 80px; color: var(--heading-ink); line-height: 1; }
  .note { position: absolute; width: 330px; text-align: center; font-family: 'Handlee', cursive; font-size: 27px; line-height: 31px; color: #4a4a3a; }
  .dash { position: absolute; border-top: 2px dashed var(--rule); }
  .dot { position: absolute; border-top: 1px dotted var(--rule); }
  .vdash { position: absolute; border-left: 1px dashed var(--rule); }
  .menu-title { position: absolute; left: 440px; top: 318px; width: 290px; text-align: center;
    font-family: 'Kaushan Script', cursive; font-weight: 400; font-size: 62px; line-height: 64px; color: var(--brown); }
  .section-head { position: absolute; text-align: center; font-family: 'Alegreya Sans SC', sans-serif; font-weight: 800; font-size: 30px; color: var(--heading-ink); line-height: 1; }
  .section-sub { position: absolute; text-align: center; font-family: 'Handlee', cursive; font-size: 18px; line-height: 20px; color: #4a4a3a; }
  .item { position: absolute; white-space: nowrap; }
  .item-name { font-family: 'Alegreya Sans SC', sans-serif; font-weight: 800; font-size: 21px; color: var(--title-green); line-height: 24px; }
  .item-desc { font-size: 15px; line-height: 19.6px; letter-spacing: -.2px; }
  .food { position: absolute; border-radius: 46% 54% 50% 50%; }
  .toast { background: radial-gradient(circle at 50% 50%, var(--food-warm), #9b7a4c 70%, rgba(155,122,76,.2)); }
  .salad { background: radial-gradient(circle at 50% 45%, var(--food-green), #5f8f34 60%, rgba(240,240,235,.6)); }
  .toppings { position: absolute; left: 607px; top: 932px; white-space: nowrap; font-size: 15.5px; line-height: 19.6px; letter-spacing: -.2px; }
  .extras { position: absolute; font-size: 15px; line-height: 24px; }
  .extras b { color: var(--accent-green); font-weight: 500; }
  .dressings { position: absolute; font-size: 15.5px; line-height: 24px; }
  .dress-head { position: absolute; left: 600px; top: 1105px; width: 500px; text-align: center;
    font-family: 'Alegreya Sans SC', sans-serif; font-weight: 800; font-size: 29px; color: var(--heading-ink); }
  .dress-head span { color: var(--accent-green); }
</style>
</head>
<body>
<main class="menu">
  <div class="leaves" role="img" aria-label="Sprig of green line-drawn leaves" style="left:0;top:15px;width:150px;height:165px;"></div>
  <div class="leaves" role="img" aria-label="Branch of green line-drawn leaves" style="left:690px;top:0;width:430px;height:150px;"></div>
  <div class="leaves" role="img" aria-label="Branch of green line-drawn leaves" style="left:0;top:1170px;width:510px;height:130px;"></div>

  <div class="brand">Mavid</div>

  <p class="note" style="left:55px;top:235px;">All Items Made to Order<br>from Open to 2pm</p>
  <div class="dash" style="left:65px;top:308px;width:310px;"></div>
  <p class="note" style="left:755px;top:235px;">All Items on Menu<br>are 100% Organic</p>
  <div class="dash" style="left:792px;top:308px;width:256px;"></div>

  <h1 class="menu-title">Breakfast<br>Menu</h1>

  <div class="dot" style="left:65px;top:410px;width:380px;"></div>
  <h2 class="section-head" style="left:60px;top:418px;width:410px;">Open Face Breakfast Toast</h2>
  <p class="section-sub" style="left:60px;top:453px;width:410px;">All Toast comes on Locally Made<br>Sourdough or Wheat Bread</p>

  <div class="vdash" style="left:588px;top:472px;height:765px;"></div>

  <div class="item" style="left:60px;top:506px;">
    <div class="item-name">Avocado Toast</div>
    <div class="item-desc">Sliced Avocado, Sliced Watermelon Radish,<br>Vine Ripened Tomatoes, Sunflower Sprouts,<br>Locally Grown Microgreens,<br>Edible Flower Petals, Olive Oil, Lemon<br>Juice, Pepper, and Himalayan Sea Salt</div>
  </div>
  <div class="item" style="left:60px;top:634px;">
    <div class="item-name">Garlic Cashew Cheese Toast</div>
    <div class="item-desc">Mavi'd Garlic Cashew Cheeze Spread,<br>Sliced Avocado, Marinated Onion Olive Oil,<br>Locally Grown Microgreens, Dried Rose Petals,<br>Edible Flower Petals, Pepper,<br>and Himalayan Sea Salt</div>
  </div>
  <div class="item" style="left:60px;top:763px;">
    <div class="item-name">Cashew Beet Toast</div>
    <div class="item-desc">Mavi'd Garlic Beet Cashew Cheeze Spread,<br>Sunflower Sprouts, Edible Flower Petals,<br>Hemp Seeds, Sprouted Pumpkin Seeds,<br>Pepper, and Himalayan Sea Salt</div>
  </div>
  <div class="item" style="left:60px;top:876px;">
    <div class="item-name">Vegan Egg Toast</div>
    <div class="item-desc">Vegan Egg Spread, Watermelon Radish,<br>Avocado Slices, Marinated Onion Olive Oil,<br>Sunflower Microgreens, Edible Flower Petals,<br>Pepper, and Kala salt</div>
  </div>
  <div class="item" style="left:60px;top:990px;">
    <div class="item-name">Peanut Butter Toast</div>
    <div class="item-desc">Mavi'd Homemade Peanut Butter,<br>Banana Slices, Strawberries, Cacao Nibs,<br>and Local Raw Honey</div>
  </div>
  <div class="item" style="left:60px;top:1078px;">
    <div class="item-name">Sprouted Almond Butter Toast</div>
    <div class="item-desc">Mavi'd Sprouted Almond Butter, Bananas,<br>Goji Berries, Cacao Chocolate Drizzle,<br>and Local Raw Honey</div>
  </div>

  <div class="food toast" role="img" aria-label="Photo of avocado toast" style="left:410px;top:530px;width:105px;height:100px;"></div>
  <div class="food toast" role="img" aria-label="Photo of garlic cashew cheese toast" style="left:418px;top:648px;width:100px;height:100px;"></div>
  <div class="food toast" role="img" aria-label="Photo of cashew beet toast" style="left:408px;top:766px;width:112px;height:100px;"></div>
  <div class="food salad" role="img" aria-label="Photo of vegan egg toast" style="left:412px;top:874px;width:105px;height:92px;"></div>
  <div class="food toast" role="img" aria-label="Photo of peanut butter banana toast" style="left:418px;top:982px;width:95px;height:85px;"></div>
  <div class="food toast" role="img" aria-label="Photo of almond butter toast" style="left:410px;top:1075px;width:105px;height:92px;"></div>

  <div class="dot" style="left:720px;top:410px;width:362px;"></div>
  <h2 class="section-head" style="left:690px;top:420px;width:380px;">100 % Organic Salads</h2>
  <p class="section-sub" style="left:690px;top:452px;width:380px;"><span style="font-size:22px;">$7.99</span> Your choice<br>of homemade organic dressings</p>

  <div class="item" style="left:608px;top:505px;">
    <div class="item-name">Asian Salad</div>
    <div class="item-desc">Kale, Spinach, Watermelon Radish,<br>Goji Berries, Sesame Seeds</div>
  </div>
  <div class="item" style="left:608px;top:578px;">
    <div class="item-name">Waldorf Salad</div>
    <div class="item-desc">Kale, Spinach, Celery, Apple, Walnuts,<br>Raisins</div>
  </div>
  <div class="item" style="left:608px;top:644px;">
    <div class="item-name">Garden Salad</div>
    <div class="item-desc">Kale, Spinach, Carrots, Beets, Tomato,<br>Cucumber</div>
  </div>
  <div class="item" style="left:608px;top:712px;">
    <div class="item-name">Kale Salad</div>
    <div class="item-desc">Kale, Strawberries, Apples, Carrots, Almonds</div>
  </div>
  <div class="item" style="left:608px;top:760px;">
    <div class="item-name">Caesar Salad</div>
    <div class="item-desc">Kale, Romaine, ....</div>
  </div>
  <div class="item" style="left:608px;top:809px;">
    <div class="item-name">Build your Own</div>
    <div class="item-desc">Your Choice of Kale, Spinach, Romaine or<br>any combo and your choice of 4 Toppings</div>
  </div>

  <div class="food salad" role="img" aria-label="Photo of Asian salad" style="left:952px;top:508px;width:88px;height:68px;"></div>
  <div class="food salad" role="img" aria-label="Photo of Waldorf salad" style="left:945px;top:585px;width:95px;height:55px;"></div>
  <div class="food salad" role="img" aria-label="Photo of garden salad" style="left:945px;top:650px;width:95px;height:58px;"></div>
  <div class="food salad" role="img" aria-label="Photo of kale salad" style="left:952px;top:718px;width:92px;height:55px;"></div>
  <div class="food salad" role="img" aria-label="Photo of Caesar salad" style="left:952px;top:785px;width:88px;height:60px;"></div>

  <div class="dash" style="left:590px;top:887px;width:495px;border-top-width:1px;"></div>
  <h2 class="section-head" style="left:600px;top:895px;width:520px;font-size:28px;">Organic Toppings</h2>
  <p class="toppings">Apple, Strawberries, Blueberries, Beets, Tomato, Cucumber, Carrots,<br>Spinach, Celery, Avocado, Watermelon Radish, Goji Berries,<br>Mulberries, Golden Berries, Raisins, Walnuts, Almonds, Pecans,<br>Sunflower Seeds, Sesame Seeds, Cashews, Bee Pollen, Chia Seeds,<br>Mango, Pineapple</p>
  <p class="extras" style="left:608px;top:1036px;">Extra Toppings <b>$2.49</b><br>Savory Walnut Ground “beef”</p>
  <p class="extras" style="left:882px;top:1036px;">Marinated Tempeh<br>Quinoa</p>

  <div class="dash" style="left:590px;top:1096px;width:495px;border-top-width:1px;"></div>
  <h2 class="dress-head"><span>100% Organic</span> Homemade Dressings</h2>
  <p class="dressings" style="left:686px;top:1150px;">Avocado Miso<br>Hemp Ranch<br>Honey Jalapeno Vinaigrette</p>
  <p class="dressings" style="left:907px;top:1150px;">Cucumber Miso<br>Fig Vinaigrette<br>Cesar Dressing</p>
</main>
</body>
</html>
```